QTR Business Card

Harborline Capital Partners is a successful and reputable financial services company.Our main services are home loans, commercial loans, vehicle finance and equipment finance. We also do development finance for property developers. Our company is always evolving to always be an industry leader in best financial service practices with access to the largest range of lenders in the country.

We want the business card to reflect our national finance company. Modern, professional corporate image. At the same time the concept of Harborline Capital Partners is that we help build wealth for you but the process for the client is an enjoyable peaceful experience. Not stressful at all .....

Colors to be same as the logo .... gold silver black white as the options

On the reverse side of the card I wanted either just the logo symbol or the logo symbol and text of the logo ....

It could be on a black background ..... or silver or gold .... want it to be quite striking to look at when you first see the card.

On the other side of the card I wanted the following details:

Doran Pelham
Director

0498 372 604

doran@hbcpx.com.au

Po Box 852
Tarrow ACT 2694

www.hbcpx.com.au

ACN 918 264 057 (This can be in very small print and can be in the bottom corner of the card or somewhere not very prominent)
Updates

As requested Ive uploaded the logo file in both .ai and .pdf formats. Please let me know if you need anything else. Thanks

Reason: Still deciding on which design I like best. I will provide individual feedback as well.

```html
<!DOCTYPE html>
<html lang="en">
<head>
<meta charset="utf-8">
<title>QTR Business Card</title>
<link rel="stylesheet" href="https://fonts.googleapis.com/css2?family=Open+Sans:ital,wght@0,400;0,700;1,400&display=swap">
<style>
  :root {
    --stage: #3b322d;
    --silver-light: #f7f7f7;
    --silver-mid: #e6e6e6;
    --silver-dark: #cfcfcf;
    --gold: #c9a23f;
    --gold-light: #e9cf7a;
    --ring-grey: #8e8e8e;
    --ink: #1c1c1c;
    --ink-soft: #333333;
  }
  * { box-sizing: border-box; margin: 0; padding: 0; }
  html, body {
    width: 1200px; height: 768px; overflow: hidden;
    background: var(--stage);
    font-family: "Open Sans", Arial, sans-serif;
  }
  .stage {
    position: relative; width: 1200px; height: 768px;
    display: flex; align-items: center; justify-content: center; gap: 60px;
  }
  .card {
    position: relative; width: 520px; height: 300px;
    background: linear-gradient(135deg, var(--silver-light) 0%, var(--silver-mid) 55%, var(--silver-dark) 100%);
    overflow: hidden;
    box-shadow: 0 10px 24px rgba(0,0,0,.35);
  }
  /* Brand lockup: plain circle beside the name */
  .brand {
    display: flex; align-items: center; gap: 14px;
  }
  .brand-circle {
    width: 64px; height: 64px; border-radius: 50%;
    border: 5px solid var(--gold);
    background: var(--silver-light);
  }
  .brand-name {
    font-weight: 700; font-size: 40px; letter-spacing: 2px;
    color: var(--gold);
  }
  .card-front { display: flex; align-items: center; justify-content: center; }

  .card-back .brand { position: absolute; left: 58px; top: 112px; }
  .card-back .brand-circle { width: 54px; height: 54px; border-width: 4px; }
  .card-back .brand-name { font-size: 32px; }

  .holder { position: absolute; left: 300px; top: 78px; }
  .holder-name { font-weight: 700; font-size: 19px; color: var(--ink); }
  .holder-title { font-size: 12px; color: var(--ink-soft); margin-top: 1px; }

  .contact-list {
    position: absolute; left: 300px; top: 150px; list-style: none;
    font-size: 13.5px; line-height: 18px; color: var(--ink);
  }
  .contact-list li { display: flex; align-items: flex-start; gap: 8px; }
  .contact-list .icon { width: 11px; height: 11px; margin-top: 3px; flex: none; fill: var(--ink); }
  .contact-list .no-icon { padding-left: 19px; }

  .gold-band {
    position: absolute; left: 0; right: 0; bottom: 0; height: 9px;
    background: linear-gradient(90deg, var(--gold), var(--gold-light) 50%, var(--gold));
  }
</style>
</head>
<body>
<main class="stage">
  <section class="card card-front" aria-label="Card front">
    <div class="brand">
      <span class="brand-circle"></span>
      <span class="brand-name">QTR</span>
    </div>
  </section>

  <section class="card card-back" aria-label="Card back">
    <div class="brand">
      <span class="brand-circle"></span>
      <span class="brand-name">QTR</span>
    </div>

    <div class="holder">
      <p class="holder-name">Doran Pelham</p>
      <p class="holder-title">Director</p>
    </div>

    <ul class="contact-list">
      <li>
        <svg class="icon" viewBox="0 0 12 12" aria-hidden="true"><path d="M1 3c0-1 1-2 2-2h6c1 0 2 1 2 2v1H8V3H4v1H1z M2 5h8l1 6H1z"/></svg>
        <span>0498 372 604</span>
      </li>
      <li>
        <svg class="icon" viewBox="0 0 12 12" aria-hidden="true"><path d="M0 2h12v8H0z M0 2l6 5 6-5" fill="var(--ink)" stroke="var(--silver-light)" stroke-width="1"/></svg>
        <span>doran@hbcpx.com.au</span>
      </li>
      <li>
        <svg class="icon" viewBox="0 0 12 12" aria-hidden="true"><path d="M6 0a4 4 0 0 1 4 4c0 3-4 8-4 8S2 7 2 4a4 4 0 0 1 4-4zm0 2.5a1.5 1.5 0 1 0 0 3 1.5 1.5 0 0 0 0-3z"/></svg>
        <span>Po Box 852</span>
      </li>
      <li class="no-icon"><span>Tarrow ACT 2694</span></li>
      <li>
        <svg class="icon" viewBox="0 0 12 12" aria-hidden="true"><circle cx="6" cy="6" r="5.5"/><path d="M0.5 6h11M6 0.5c-3 3-3 8 0 11M6 0.5c3 3 3 8 0 11" stroke="var(--silver-light)" stroke-width="0.8" fill="none"/></svg>
        <span>www.hbcpx.com.au</span>
      </li>
      <li class="no-icon"><span>ACN 918 264 057</span></li>
    </ul>

    <div class="gold-band"></div>
  </section>
</main>
</body>
</html>
```